Website Needs a New Look & Feel - I am Too Old and Uncool on my Own

I want some design ideas for my current site. I need a new, more modern and dynamic look and feel. The audience for the site is 90% male, 24-54 years old, and not highly educated. English is second language for about 30% of audience, so images help. 85% of visitors view on mobile. We sell trucks and trailers to this audience. . Just want something new and cool. Tired of what I have. Current site doesn't seem strong enough to match the kind of people who drive trucks for a living. Current is site is vornels.com. Pull relevant menu and text from the site.

Target Market(s)

Truck Drivers and Trucking Company Owners (90% male).

Industry/Entity Type

Transportation - Specifically, truck and trailer sales.

Number of Pages Required

3 page

Font styles to use
Sans Serif

Colors
0054AA
0677BA
7BADD7
CADEEF
E8F1F8

Requirements
Must have
• Images of Sleeper Trucks (like on there now) and trailers. Audience is very literal, so they need to see what we sell.
Nice to have
• Images of Sleeper Trucks (like on tMy inventory pages are boring, please show me something more user-friendly and interesting. here now) and trailers.

```html
<!DOCTYPE html>
<html lang="en">
<head>
<meta charset="utf-8">
<title>Vornels Truck &amp; Trailer – Web and Mobile Layouts</title>
<link href="https://fonts.googleapis.com/css2?family=Montserrat:wght@600;700;800;900&family=Open+Sans:wght@400;600;700&display=swap" rel="stylesheet">
<style>
:root{
  --navy:#0b1733;
  --navy-2:#13244d;
  --blue:#0054aa;
  --blue-bright:#1f5fd6;
  --blue-mid:#0677ba;
  --blue-soft:#7badd7;
  --blue-pale:#cadeef;
  --blue-wash:#e8f1f8;
  --ink:#1b2230;
  --grey:#6b7280;
  --line:#d6dbe3;
  --white:#ffffff;
}
*{box-sizing:border-box;margin:0;padding:0}
html,body{width:1200px;height:2764px;overflow:hidden}
body{background:var(--white);font-family:"Open Sans",Arial,sans-serif;color:var(--ink);position:relative}
h1,h2,h3,h4,.brand,.btn{font-family:"Montserrat",Arial,sans-serif}
.version-label{position:absolute;top:30px;font-family:"Montserrat",sans-serif;font-weight:700;font-size:22px;color:var(--ink)}
.section{position:relative;overflow:hidden}
.photo{position:absolute}
/* product photo areas: sky, chrome body, asphalt */
.photo-truck{background:
  linear-gradient(180deg,rgba(255,255,255,0) 0%,rgba(255,255,255,0) 72%,#4a4f58 72%,#2f333a 100%),
  radial-gradient(ellipse 55% 45% at 55% 52%,#f4f6f9 0%,#c3ccd8 45%,rgba(195,204,216,0) 75%),
  linear-gradient(180deg,#8fb3dc 0%,#d8e4f1 70%)}
.photo-trailer{background:
  linear-gradient(180deg,rgba(255,255,255,0) 0%,rgba(255,255,255,0) 78%,#9aa3ae 78%,#7d8692 100%),
  linear-gradient(180deg,rgba(255,255,255,0) 22%,#ffffff 22%,#eef1f5 60%,#d5dbe3 78%),
  linear-gradient(180deg,#c9dcef 0%,#eef4fa 100%)}
.photo-night{background:
  radial-gradient(ellipse 40% 50% at 70% 55%,#c7d2e2 0%,#6f87ad 40%,rgba(20,40,90,0) 75%),
  linear-gradient(180deg,#0a1636 0%,#173466 60%,#0d1c40 100%)}
.photo-yard{background:
  linear-gradient(180deg,rgba(255,255,255,0) 0%,rgba(255,255,255,0) 70%,#6f6a62 70%,#55514b 100%),
  linear-gradient(90deg,#d9dee6 0%,#a9b5c6 25%,#e6eaf0 50%,#97a6ba 75%,#d9dee6 100%)}
.photo-crane{background:
  linear-gradient(180deg,rgba(255,255,255,0) 0%,rgba(255,255,255,0) 55%,#e0b73e 55%,#b58f2a 80%,#6a6d72 80%,#55585d 100%),
  linear-gradient(180deg,#dfe8f2 0%,#f5f7fa 100%)}
.photo-red{background:
  linear-gradient(180deg,rgba(255,255,255,0) 0%,rgba(255,255,255,0) 74%,#5a5f66 74%,#43474d 100%),
  radial-gradient(ellipse 50% 40% at 50% 55%,#d4483c 0%,#a8352d 50%,rgba(168,53,45,0) 80%),
  linear-gradient(180deg,#a3bcd6 0%,#d3e0ec 100%)}
.btn{display:inline-block;background:var(--blue-bright);color:var(--white);font-weight:700;text-transform:uppercase;letter-spacing:.04em}
.brand{font-weight:900;color:var(--navy);line-height:1;display:flex;align-items:center;gap:6px}
.brand .mark{width:10px;height:10px;background:var(--blue-bright)}
.brand-light{color:var(--white)}
.tick{flex:none;display:block}

/* ---------- Web page ---------- */
.web{position:absolute;left:32px;top:88px;width:768px;height:2672px;box-shadow:0 0 0 1px var(--line)}
.web .header{height:72px;display:flex;align-items:center;justify-content:space-between;padding:0 40px;background:var(--white)}
.web .brand{font-size:18px}
.web .nav{display:flex;gap:18px;font-size:7px;font-weight:700;text-transform:uppercase;color:var(--ink)}
.web .nav .active{color:var(--blue-bright)}
.web .contact-mini{font-size:7px;color:var(--grey);display:flex;gap:10px}
.web .hero{height:280px;background:var(--navy)}
.web .hero .photo{inset:0}
.web .hero-copy{position:absolute;left:40px;top:80px;width:300px;color:var(--white)}
.web .hero-copy h1{font-size:27px;font-weight:900;line-height:1.1;text-transform:uppercase}
.web .hero-copy p{font-size:7px;margin:10px 0 14px;opacity:.85}
.web .hero-copy .btn{font-size:7px;padding:7px 14px}
.web svg.edge{position:absolute;left:0;bottom:0;width:100%}
.web .about{height:300px;background:var(--white)}
.web .about-copy{position:absolute;left:40px;top:30px;width:240px}
.web h2{font-size:18px;font-weight:800;text-transform:uppercase;color:var(--navy)}
.web .about-copy p{font-size:7px;line-height:1.6;color:var(--grey);margin-top:10px}
.web .about-copy .btn{font-size:7px;padding:7px 14px;margin-top:14px}
.web .about .photo{left:300px;top:10px;width:430px;height:270px;border-radius:4px}
.web .categories{height:180px;display:flex;gap:14px;padding:10px 40px}
.web .cat{flex:1;position:relative}
.web .cat .photo{left:0;right:0;top:0;height:110px}
.web .cat span{position:absolute;left:0;right:0;top:118px;background:var(--blue-bright);color:var(--white);font-family:"Montserrat",sans-serif;font-size:7px;font-weight:700;text-align:center;padding:6px 0;text-transform:uppercase}
.web .prices{height:400px;background:var(--navy)}
.web svg.bg{position:absolute;left:0;top:0}
.web .prices h2{position:absolute;top:140px;width:100%;text-align:center;color:var(--white)}
.web .reasons{position:absolute;left:60px;right:60px;top:190px;display:flex;gap:20px}
.web .reason{flex:1;background:var(--white);padding:14px;display:flex;gap:8px;font-size:7px;color:var(--grey);line-height:1.5;align-items:flex-start}
.web .reason .tick{width:14px;height:14px}
.web .features{height:360px;background:var(--white)}
.web .feature{position:absolute;left:60px;right:60px;height:140px;display:flex;gap:24px;align-items:center}
.web .feature .photo{position:relative;width:300px;height:140px;flex:none}
.web .feature h3{font-size:11px;font-weight:800;text-transform:uppercase;color:var(--navy);line-height:1.2}
.web .feature p{font-size:7px;color:var(--grey);line-height:1.6;margin:8px 0}
.web .feature .btn{font-size:6px;padding:6px 12px}
.web .equipment{height:200px;background:var(--navy)}
.web .equipment h2{position:absolute;top:86px;width:100%;text-align:center;color:var(--white);font-size:15px}
.web .blog{height:420px;background:var(--white);text-align:center}
.web .blog h2{margin-top:40px}
.web .blog-grid{display:flex;gap:12px;padding:24px 60px 0}
.web .post{flex:1;height:200px;position:relative}
.web .post .photo{inset:0}
.web .post-caption{position:absolute;left:0;right:0;bottom:0;background:rgba(11,23,51,.85);color:var(--white);padding:10px;text-align:left}
.web .post-caption h4{font-size:7px;font-weight:700;text-transform:uppercase;line-height:1.3}
.web .post-caption .btn{font-size:5px;padding:4px 8px;margin-top:6px}
.web .blog .more{font-size:7px;padding:7px 16px;margin-top:24px}
.web .contact{height:260px;background:var(--blue-wash)}
.web .contact-card{position:absolute;left:140px;right:140px;top:30px;height:210px;background:var(--white);padding:20px 30px;text-align:center;box-shadow:0 2px 8px rgba(0,0,0,.08)}
.web .contact-card h2{font-size:14px}
.web .fields{display:grid;grid-template-columns:1fr 1fr;gap:8px;margin-top:16px}
.web .field{height:20px;border:1px solid var(--line);font-size:6px;color:var(--grey);text-align:left;padding:6px;line-height:1}
.web .field.wide{grid-column:1/3;height:44px}
.web .contact-card .btn{font-size:6px;padding:6px 20px;margin-top:12px}
.web .footer{height:200px;background:var(--navy);color:var(--white);text-align:center;padding-top:40px}
.web .footer .brand{justify-content:center;font-size:20px}
.web .footer-nav{display:flex;justify-content:center;gap:22px;font-size:7px;font-weight:700;text-transform:uppercase;margin-top:22px}
.web .footer-contact{display:flex;justify-content:center;gap:24px;font-size:7px;margin-top:16px;opacity:.85}
.web .copyright{font-size:6px;opacity:.6;margin-top:24px}

/* ---------- Mobile page ---------- */
.mobile{position:absolute;top:88px;width:172px;height:2672px;box-shadow:0 0 0 1px var(--line)}
.mobile-a{left:828px}
.mobile-b{left:1012px}
.mobile .header{height:72px;display:flex;align-items:center;justify-content:space-between;padding:0 12px;background:var(--white)}
.mobile .brand{font-size:14px}
.mobile .menu{width:18px;height:18px;border-radius:50%;background:var(--blue-bright)}
.mobile h2{font-size:15px;font-weight:800;text-transform:uppercase;color:var(--navy);text-align:center}
.mobile p{font-size:6px;line-height:1.6;color:var(--grey)}
.mobile .btn{font-size:5px;padding:5px 10px}
.mobile .hero{height:220px;background:var(--navy)}
.mobile .hero .photo{inset:0}
.mobile .hero-copy{position:absolute;left:12px;right:12px;top:40px;text-align:center;color:var(--white)}
.mobile .hero-copy h1{font-size:15px;font-weight:900;line-height:1.1;text-transform:uppercase}
.mobile .hero-copy p{color:var(--white);opacity:.85;margin:8px 0}
.mobile svg.edge{position:absolute;left:0;bottom:0;width:100%}
.mobile .about{height:300px;padding:24px 14px;text-align:center}
.mobile .about p{margin:8px 0}
.mobile .truck{height:240px}
.mobile .truck .photo{inset:10px 0}
.mobile .cat{height:280px;padding:20px 14px}
.mobile .cat .photo{left:14px;right:14px;top:20px;height:200px}
.mobile .cat span{position:absolute;left:14px;right:14px;top:226px;background:var(--blue-bright);color:var(--white);font-family:"Montserrat",sans-serif;font-size:6px;font-weight:700;text-align:center;padding:6px 0;text-transform:uppercase}
.mobile .prices{height:720px;background:var(--navy)}
.mobile svg.bg{position:absolute;left:0;top:0}
.mobile .prices h2{position:relative;color:var(--white);font-size:20px;text-align:left;padding:90px 14px 0;line-height:1.1}
.mobile .reason{position:relative;margin:14px 14px 0;background:var(--white);padding:10px;display:flex;gap:6px;align-items:flex-start}
.mobile .reason .tick{width:12px;height:12px}
.mobile .feature{height:260px;padding:0 14px}
.mobile .feature .photo{left:14px;right:14px;top:10px;height:100px}
.mobile .feature .copy{position:absolute;left:14px;right:14px;top:120px;text-align:center}
.mobile .feature h3{font-size:9px;font-weight:800;text-transform:uppercase;color:var(--navy);line-height:1.2}
.mobile .feature p{margin:6px 0}
.mobile .equipment{height:180px;background:var(--blue-bright)}
.mobile .equipment h2{position:absolute;top:60px;left:10px;right:10px;color:var(--white);font-size:12px;line-height:1.2}
.mobile .blog{height:1090px;background:var(--navy);padding:30px 14px 0}
.mobile .blog h2{color:var(--white);margin-bottom:16px}
.mobile .post{position:relative;height:228px;margin-bottom:22px}
.mobile .post .photo{inset:0}
.mobile .post-caption{position:absolute;left:0;right:0;bottom:0;background:rgba(11,23,51,.85);color:var(--white);padding:8px}
.mobile .post-caption h4{font-size:6px;font-weight:700;text-transform:uppercase}
.mobile .post-caption .btn{margin-top:5px;font-size:4px;padding:3px 6px}
.mobile .blog .more{display:block;width:70px;margin:0 auto;text-align:center}
.mobile .contact{height:600px;background:var(--blue-wash);padding:20px 10px}
.mobile .contact-card{background:var(--white);height:560px;padding:20px 10px;text-align:center}
.mobile .field{height:28px;border:1px solid var(--line);font-size:5px;color:var(--grey);text-align:left;padding:10px 6px;margin-top:12px;line-height:1}
.mobile .field.wide{height:150px}
.mobile .contact-card .btn{margin-top:16px;padding:6px 18px}
.mobile .footer{height:282px;background:var(--navy);color:var(--white);text-align:center;padding:40px 14px 0}
.mobile .footer .brand{justify-content:center;font-size:16px}
.mobile .footer-nav{display:grid;grid-template-columns:1fr 1fr;gap:8px;font-size:6px;font-weight:700;text-transform:uppercase;margin-top:22px}
.mobile .footer-contact{font-size:6px;margin-top:20px;opacity:.85;line-height:1.8}
.mobile .copyright{font-size:5px;opacity:.6;margin-top:24px}
</style>
</head>
<body>

<div class="version-label" style="left:32px">Web Version</div>
<div class="version-label" style="left:828px">Mobile Version</div>

<!-- ================= Web page ================= -->
<main class="web">
  <header class="header">
    <div class="brand"><span class="mark"></span>VORNELS</div>
    <nav class="nav"><span class="active">Home</span><span>About</span><span>Inventory</span><span>Financing</span><span>Blog</span><span>Contact</span></nav>
    <div class="contact-mini"><span>(555) 014-2290</span><span>info@vornels.com</span></div>
  </header>

  <section class="section hero">
    <div class="photo photo-night" role="img" aria-label="Photo: front view of a chrome sleeper semi truck at night"></div>
    <div class="hero-copy">
      <h1>Wholesale Trucks &amp; Trailers Save Thousands</h1>
      <p>Quality used sleepers, reefers and dry vans at wholesale prices for drivers and fleets.</p>
      <span class="btn">View Inventory</span>
    </div>
    <svg class="edge" viewBox="0 0 768 60" height="60" preserveAspectRatio="none">
      <polygon points="0,20 768,50 768,60 0,60" fill="var(--blue-bright)"/>
      <polygon points="0,34 768,58 768,60 0,60" fill="var(--white)"/>
    </svg>
  </section>

  <section class="section about">
    <div class="about-copy">
      <h2>About Us</h2>
      <p>Vornels Truck &amp; Trailer is a trusted dealership serving owner operators and fleets. We buy in volume and pass the savings to you, so every truck on our lot is priced well below retail.</p>
      <p>Our team inspects each unit, handles the paperwork and helps you find financing, so you can get back on the road fast.</p>
      <span class="btn">Learn More</span>
    </div>
    <div class="photo photo-truck" role="img" aria-label="Photo: silver sleeper semi truck, three-quarter front view"></div>
  </section>

  <section class="section categories">
    <div class="cat"><div class="photo photo-trailer" role="img" aria-label="Photo: white reefer trailer"></div><span>Reefer Trailers</span></div>
    <div class="cat"><div class="photo photo-truck" role="img" aria-label="Photo: sleeper truck"></div><span>Sleepers</span></div>
    <div class="cat"><div class="photo photo-trailer" role="img" aria-label="Photo: white dry van trailer"></div><span>Dry Vans</span></div>
    <div class="cat"><div class="photo photo-crane" role="img" aria-label="Photo: yellow crane truck"></div><span>Cranes</span></div>
  </section>

  <section class="section prices">
    <svg class="bg" viewBox="0 0 768 400" width="768" height="400" preserveAspectRatio="none">
      <polygon points="0,0 768,0 768,60 0,110" fill="var(--white)"/>
      <polygon points="0,110 300,70 0,190" fill="var(--blue)"/>
      <polygon points="768,60 470,100 768,200" fill="var(--blue-bright)"/>
      <polygon points="0,400 768,400 768,340 0,380" fill="var(--white)"/>
      <polygon points="0,380 768,340 768,320 0,360" fill="var(--blue)"/>
    </svg>
    <h2>How Are the Prices So Low?</h2>
    <div class="reasons">
      <div class="reason"><svg class="tick" viewBox="0 0 14 14"><circle cx="7" cy="7" r="7" fill="var(--blue-bright)"/><path d="M4 7.2l2 2 4-4.4" stroke="#fff" stroke-width="1.6" fill="none"/></svg><span>We buy large groups of equipment from fleets and pass the savings on to you.</span></div>
      <div class="reason"><svg class="tick" viewBox="0 0 14 14"><circle cx="7" cy="7" r="7" fill="var(--blue-bright)"/><path d="M4 7.2l2 2 4-4.4" stroke="#fff" stroke-width="1.6" fill="none"/></svg><span>We keep a lean team and low overhead, so our prices stay low every day.</span></div>
      <div class="reason"><svg class="tick" viewBox="0 0 14 14"><circle cx="7" cy="7" r="7" fill="var(--blue-bright)"/><path d="M4 7.2l2 2 4-4.4" stroke="#fff" stroke-width="1.6" fill="none"/></svg><span>We sell at wholesale volume with a small margin on every single unit.</span></div>
    </div>
  </section>

  <section class="section features">
    <div class="feature" style="top:30px">
      <div class="photo photo-yard" role="img" aria-label="Photo: row of sleeper trucks on the sales lot"></div>
      <div><h3>Wholesale Reefers, Dry Vans &amp; Sleepers</h3><p>Browse a large stock of ready to work trucks and trailers, inspected and priced to move quickly.</p><span class="btn">Shop Now</span></div>
    </div>
    <div class="feature" style="top:190px">
      <div><h3>Buying From Vornels Truck &amp; Trailer</h3><p>Simple steps, honest pricing and help with financing. Call us today and drive away this week.</p><span class="btn">Learn More</span></div>
      <div class="photo photo-night" role="img" aria-label="Photo: semi truck with trailer on the highway"></div>
    </div>
  </section>

  <section class="section equipment">
    <svg class="bg" viewBox="0 0 768 200" width="768" height="200" preserveAspectRatio="none">
      <polygon points="0,0 768,0 768,20 384,60 0,20" fill="var(--white)"/>
      <polygon points="0,20 384,60 768,20 768,50 384,90 0,50" fill="var(--blue-bright)"/>
      <polygon points="0,200 768,200 768,180 384,150 0,180" fill="var(--white)"/>
      <polygon points="0,180 384,150 768,180 768,160 384,130 0,160" fill="var(--blue)"/>
    </svg>
    <h2>Have More Equipment Than You Need?</h2>
  </section>

  <section class="section blog">
    <h2>Latest Blog</h2>
    <div class="blog-grid">
      <div class="post"><div class="photo photo-trailer" role="img" aria-label="Photo: reefer trailer"></div><div class="post-caption"><h4>Choosing the right reefer trailer</h4><span class="btn">Read More</span></div></div>
      <div class="post"><div class="photo photo-yard" role="img" aria-label="Photo: trucks parked in a yard"></div><div class="post-caption"><h4>Tips for buying a used sleeper</h4><span class="btn">Read More</span></div></div>
      <div class="post"><div class="photo photo-red" role="img" aria-label="Photo: red semi truck"></div><div class="post-caption"><h4>Keeping your truck road ready</h4><span class="btn">Read More</span></div></div>
      <div class="post"><div class="photo photo-trailer" role="img" aria-label="Photo: dry van trailer"></div><div class="post-caption"><h4>Dry van or reefer for your loads</h4><span class="btn">Read More</span></div></div>
    </div>
    <span class="btn more">View All</span>
  </section>

  <section class="section contact">
    <div class="contact-card">
      <h2>Contact Us</h2>
      <div class="fields">
        <div class="field">First Name</div><div class="field">Last Name</div>
        <div class="field">Email</div><div class="field">Phone</div>
        <div class="field wide">Message</div>
      </div>
      <span class="btn">Submit</span>
    </div>
  </section>

  <footer class="footer">
    <div class="brand brand-light"><span class="mark"></span>VORNELS</div>
    <nav class="footer-nav"><span>Home</span><span>About</span><span>Inventory</span><span>Financing</span><span>Blog</span><span>Contact</span></nav>
    <div class="footer-contact"><span>(555) 014-2290</span><span>info@vornels.com</span></div>
    <div class="copyright">Copyright © Vornels Truck &amp; Trailer</div>
  </footer>
</main>

<!-- ================= Mobile page, part one ================= -->
<main class="mobile mobile-a">
  <header class="header">
    <div class="brand"><span class="mark"></span>VORNELS</div>
    <span class="menu"></span>
  </header>

  <section class="section hero">
    <div class="photo photo-night" role="img" aria-label="Photo: front view of a chrome sleeper semi truck at night"></div>
    <div class="hero-copy">
      <h1>Wholesale Trucks &amp; Trailers Save Thousands</h1>
      <p>Quality used trucks at wholesale prices.</p>
      <span class="btn">View Inventory</span>
    </div>
    <svg class="edge" viewBox="0 0 172 40" height="40" preserveAspectRatio="none">
      <polygon points="0,10 172,30 172,40 0,40" fill="var(--blue-bright)"/>
      <polygon points="0,22 172,38 172,40 0,40" fill="var(--white)"/>
    </svg>
  </section>

  <section class="section about">
    <h2>About Us</h2>
    <p>Vornels Truck &amp; Trailer is a trusted dealership serving owner operators and fleets. We buy in volume and pass the savings to you.</p>
    <p>Every unit is inspected, and our team helps with paperwork and financing so you get back on the road fast.</p>
    <span class="btn">Learn More</span>
  </section>

  <section class="section truck"><div class="photo photo-truck" role="img" aria-label="Photo: silver sleeper semi truck"></div></section>

  <section class="section cat"><div class="photo photo-trailer" role="img" aria-label="Photo: white reefer trailer"></div><span>Reefer Trailers</span></section>
  <section class="section cat"><div class="photo photo-truck" role="img" aria-label="Photo: sleeper truck"></div><span>Sleepers</span></section>
  <section class="section cat"><div class="photo photo-trailer" role="img" aria-label="Photo: white dry van trailer"></div><span>Dry Vans</span></section>
  <section class="section cat"><div class="photo photo-crane" role="img" aria-label="Photo: yellow crane truck"></div><span>Cranes</span></section>

  <section class="section prices">
    <svg class="bg" viewBox="0 0 172 720" width="172" height="720" preserveAspectRatio="none">
      <polygon points="0,0 172,0 172,20 0,60" fill="var(--white)"/>
      <polygon points="0,60 172,20 172,50 0,80" fill="var(--blue)"/>
    </svg>
    <h2>How Are the Prices So Low?</h2>
    <div class="reason"><svg class="tick" viewBox="0 0 14 14"><circle cx="7" cy="7" r="7" fill="var(--blue-bright)"/><path d="M4 7.2l2 2 4-4.4" stroke="#fff" stroke-width="1.6" fill="none"/></svg><p>We buy large groups of equipment from fleets and pass savings on to you.</p></div>
    <div class="reason"><svg class="tick" viewBox="0 0 14 14"><circle cx="7" cy="7" r="7" fill="var(--blue-bright)"/><path d="M4 7.2l2 2 4-4.4" stroke="#fff" stroke-width="1.6" fill="none"/></svg><p>A lean team and low overhead keep our prices low every day.</p></div>
    <div class="reason"><svg class="tick" viewBox="0 0 14 14"><circle cx="7" cy="7" r="7" fill="var(--blue-bright)"/><path d="M4 7.2l2 2 4-4.4" stroke="#fff" stroke-width="1.6" fill="none"/></svg><p>We sell at volume with a small margin on every unit.</p></div>
  </section>
</main>

<!-- ================= Mobile page, part two ================= -->
<main class="mobile mobile-b">
  <section class="section feature">
    <div class="photo photo-yard" role="img" aria-label="Photo: row of sleeper trucks on the sales lot"></div>
    <div class="copy"><h3>Wholesale Reefers, Dry Vans &amp; Sleepers</h3><p>A large stock of ready to work trucks and trailers, inspected and priced to move.</p><span class="btn">Shop Now</span></div>
  </section>
  <section class="section feature">
    <div class="photo photo-night" role="img" aria-label="Photo: semi truck with trailer on the highway"></div>
    <div class="copy"><h3>Buying From Vornels Truck &amp; Trailer</h3><p>Simple steps, honest pricing and help with financing.</p><span class="btn">Learn More</span></div>
  </section>

  <section class="section equipment">
    <svg class="bg" viewBox="0 0 172 180" width="172" height="180" preserveAspectRatio="none">
      <polygon points="0,0 172,0 172,10 86,40 0,10" fill="var(--white)"/>
      <polygon points="0,180 172,180 172,170 86,145 0,170" fill="var(--navy)"/>
    </svg>
    <h2>Have More Equipment Than You Need?</h2>
  </section>

  <section class="section blog">
    <h2>Latest Blog</h2>
    <div class="post"><div class="photo photo-trailer" role="img" aria-label="Photo: reefer trailer"></div><div class="post-caption"><h4>Choosing the right reefer trailer</h4><span class="btn">Read More</span></div></div>
    <div class="post"><div class="photo photo-yard" role="img" aria-label="Photo: trucks parked in a yard"></div><div class="post-caption"><h4>Tips for buying a used sleeper</h4><span class="btn">Read More</span></div></div>
    <div class="post"><div class="photo photo-trailer" role="img" aria-label="Photo: dry van trailer"></div><div class="post-caption"><h4>Dry van or reefer for your loads</h4><span class="btn">Read More</span></div></div>
    <div class="post"><div class="photo photo-red" role="img" aria-label="Photo: red semi truck"></div><div class="post-caption"><h4>Keeping your truck road ready</h4><span class="btn">Read More</span></div></div>
    <span class="btn more">View All</span>
  </section>

  <section class="section contact">
    <div class="contact-card">
      <h2>Contact Us</h2>
      <div class="field">First Name</div>
      <div class="field">Last Name</div>
      <div class="field">Email</div>
      <div class="field">Phone</div>
      <div class="field wide">Message</div>
      <span class="btn">Submit</span>
    </div>
  </section>

  <footer class="footer">
    <div class="brand brand-light"><span class="mark"></span>VORNELS</div>
    <nav class="footer-nav"><span>Home</span><span>About</span><span>Inventory</span><span>Financing</span><span>Blog</span><span>Contact</span></nav>
    <div class="footer-contact">(555) 014-2290<br>info@vornels.com</div>
    <div class="copyright">Copyright © Vornels Truck &amp; Trailer</div>
  </footer>
</main>

</body>
</html>
```